Post Lockdown Ortho Special

We are running a special for (Ortho) Braces/Clear Aligner (Quorventa), till July 31st 2020. Up to $2,000 off with free Consultation and Xrays.

We need a ad to run in different formats.

Maybe something with: what better time to get braces when you have to wear a mask all the time.

Trying to rebuild our business and get people in for free consultations.

```html
<!DOCTYPE html>
<html lang="en">
<head>
<meta charset="utf-8">
<title>Pinecrest Family Dentistry – Ortho Special</title>
<link href="https://fonts.googleapis.com/css2?family=Oswald:wght@500;600;700&family=Open+Sans:wght@400;600;700&display=swap" rel="stylesheet">
<style>
  :root{
    --purple:#6a3fa0;
    --purple-deep:#4f2c82;
    --lilac:#b99ad6;
    --lilac-soft:#d9c8ea;
    --ink:#4a4a52;
    --ink-soft:#6b6b73;
    --paper:#f1f1f3;
    --white:#ffffff;
    --rule:#c9c9cf;
  }
  html,body{margin:0;padding:0;overflow:hidden;background:var(--white);}
  .flyer{position:relative;width:1010px;height:1200px;overflow:hidden;background:var(--paper);font-family:"Open Sans",Arial,sans-serif;color:var(--ink);}
  .hero-photo{position:absolute;left:0;top:0;width:1010px;height:560px;
    background:linear-gradient(160deg,#e9e3d8 0%,#cdb79a 30%,#a47a5c 55%,#7b5a49 75%,#b9a38c 100%);}
  .shapes{position:absolute;left:0;top:0;width:1010px;height:1200px;}
  .tagline{position:absolute;right:28px;top:340px;width:360px;text-align:center;
    font-family:"Oswald",Arial,sans-serif;font-weight:500;font-size:23px;line-height:33px;
    color:var(--white);text-transform:uppercase;letter-spacing:.3px;}
  .brand{position:absolute;left:36px;top:470px;display:flex;align-items:center;gap:18px;}
  .brand-dot{width:74px;height:74px;border-radius:50%;background:var(--lilac-soft);}
  .brand-name{font-weight:600;font-size:29px;color:var(--purple);line-height:1.1;}
  .brand-doctor{font-size:15px;color:var(--ink-soft);letter-spacing:1.5px;text-transform:uppercase;margin-top:6px;}
  .offer{position:absolute;left:52px;display:flex;align-items:flex-start;gap:18px;}
  .offer-rate{font-family:"Oswald",Arial,sans-serif;font-weight:600;font-size:72px;line-height:1;color:var(--purple);}
  .offer-title{font-weight:700;font-size:32px;line-height:40px;color:var(--ink);text-transform:uppercase;}
  .accent{color:var(--purple);}
  .accent-soft{color:var(--lilac);}
  .expires{font-size:14px;color:var(--ink);margin-top:4px;}
  .offer--braces{top:655px;}
  .offer--aligner{top:815px;}
  .offer--aligner .offer-rate{margin-top:8px;}
  .offer--consult{top:950px;left:58px;display:block;}
  .offer--consult .offer-title{font-size:33px;line-height:44px;}
  .divider{position:absolute;left:52px;width:640px;border-top:1px dotted var(--rule);}
  .contact{position:absolute;left:0;top:1128px;width:1010px;display:flex;justify-content:space-between;
    padding:0 50px 0 64px;box-sizing:border-box;font-size:19px;color:var(--white);}
  .contact-item{display:flex;align-items:center;gap:10px;}
  .contact-icon{width:24px;height:24px;border-radius:4px;background:var(--purple-deep);display:flex;align-items:center;justify-content:center;}
</style>
</head>
<body>
<div class="flyer">
  <div class="hero-photo" role="img" aria-label="Photo of a group of smiling teenage friends hugging outdoors in warm sunlight"></div>

  <svg class="shapes" viewBox="0 0 1010 1200" xmlns="http://www.w3.org/2000/svg">
    <defs>
      <linearGradient id="band" x1="0" y1="0" x2="1" y2="1">
        <stop offset="0" stop-color="#7a4fb2"/>
        <stop offset="1" stop-color="#5c3591"/>
      </linearGradient>
      <linearGradient id="skin" x1="0" y1="0" x2="1" y2="1">
        <stop offset="0" stop-color="#f3d2c2"/>
        <stop offset="1" stop-color="#d99b86"/>
      </linearGradient>
      <linearGradient id="xray" x1="0" y1="0" x2="0" y2="1">
        <stop offset="0" stop-color="#2a2a2e"/>
        <stop offset="1" stop-color="#8a8a90"/>
      </linearGradient>
    </defs>
    <!-- purple swoosh wedge -->
    <path d="M420 560 C600 470 800 360 1010 282 L1010 740 C950 700 880 640 820 595 Z" fill="url(#band)"/>
    <!-- white logo band -->
    <path d="M0 418 C260 440 560 470 760 560 C800 580 830 600 860 620 L860 700 L0 700 Z" fill="var(--white)"/>
    <!-- grey arc under logo band -->
    <path d="M0 640 C300 700 620 690 860 560" fill="none" stroke="#cfcfd4" stroke-width="10"/>
    <path d="M0 655 C300 712 620 700 860 575 L860 1200 L0 1200 Z" fill="var(--paper)"/>
    <!-- footer band -->
    <path d="M0 1082 C300 1125 650 1110 1010 1060 L1010 1200 L0 1200 Z" fill="var(--lilac)"/>
    <path d="M0 1092 C300 1138 650 1124 1010 1074 L1010 1200 L0 1200 Z" fill="url(#band)"/>
    <!-- photo circles -->
    <circle cx="858" cy="985" r="120" fill="var(--lilac-soft)"/>
    <g role="img" aria-label="Close-up photo of a hand inserting a clear aligner tray">
      <circle cx="858" cy="578" r="118" fill="var(--lilac-soft)"/>
      <circle cx="858" cy="578" r="108" fill="url(#skin)"/>
    </g>
    <g role="img" aria-label="Close-up photo of a smile with metal braces">
      <circle cx="858" cy="786" r="118" fill="var(--lilac)"/>
      <circle cx="858" cy="786" r="108" fill="url(#skin)"/>
    </g>
    <g role="img" aria-label="Panoramic dental x-ray of a full set of teeth">
      <circle cx="858" cy="985" r="108" fill="url(#xray)"/>
    </g>
  </svg>

  <div class="tagline">What better time to get<br>braces when you have<br>to wear a mask all the time</div>

  <div class="brand">
    <div class="brand-dot"></div>
    <div>
      <div class="brand-name">Pinecrest Family Dentistry</div>
      <div class="brand-doctor">Dr Maren Holloway</div>
    </div>
  </div>

  <div class="offer offer--braces">
    <div class="offer-rate">25%</div>
    <div>
      <div class="offer-title">(Ortho) <span class="accent">Braces</span> Special</div>
      <div class="expires">expires July 31st 2020</div>
    </div>
  </div>
  <div class="divider" style="top:748px"></div>

  <div class="offer offer--aligner">
    <div class="offer-rate">30%</div>
    <div>
      <div class="offer-title">Clear Aligner<br><span class="accent">(Quorventa)</span> Special</div>
      <div class="expires">expires July 31st 2020</div>
    </div>
  </div>
  <div class="divider" style="top:932px"></div>

  <div class="offer offer--consult">
    <div class="offer-title">Up to <span class="accent-soft">$2,000 off</span> with<br><span class="accent">Free consultation and xrays</span></div>
    <div class="expires">expires July 31st 2020</div>
  </div>

  <div class="contact">
    <div class="contact-item">
      <span class="contact-icon"><svg width="12" height="14" viewBox="0 0 12 14"><path d="M6 0a5 5 0 0 0-5 5c0 3.6 5 9 5 9s5-5.4 5-9a5 5 0 0 0-5-5zm0 7a2 2 0 1 1 0-4 2 2 0 0 1 0 4z" fill="#fff"/></svg></span>
      418 N Aspen Ridge Rd, Juniper, AZ 86099
    </div>
    <div class="contact-item">
      <span class="contact-icon"><svg width="13" height="13" viewBox="0 0 24 24"><path d="M6.6 10.8a15 15 0 0 0 6.6 6.6l2.2-2.2a1 1 0 0 1 1-.25 11.4 11.4 0 0 0 3.6.57 1 1 0 0 1 1 1V20a1 1 0 0 1-1 1A17 17 0 0 1 3 4a1 1 0 0 1 1-1h3.5a1 1 0 0 1 1 1c0 1.25.2 2.45.57 3.57a1 1 0 0 1-.25 1z" fill="#fff"/></svg></span>
      (555) 014-2278
    </div>
    <div class="contact-item">
      <span class="contact-icon"><svg width="14" height="14" viewBox="0 0 14 14"><circle cx="7" cy="7" r="6" fill="none" stroke="#fff" stroke-width="1.3"/><ellipse cx="7" cy="7" rx="2.6" ry="6" fill="none" stroke="#fff" stroke-width="1.1"/><line x1="1" y1="7" x2="13" y2="7" stroke="#fff" stroke-width="1.1"/></svg></span>
      www.pinecrestsmiles.example
    </div>
  </div>
</div>
</body>
</html>
```